Kovaridex Website

we need a web site similar to Zumwarp.com or Ostrix9 com or brackfield.com - Although our budget is small we would like to look like them. we are in the same industry
Reason: Can you do an exact copy of Zumwarp.com if so how long ? What do you require? What is the next step?Please let me know you can also email me at tolvaburn@pexmail.com for faster answers.
Thank you
Target Market(s)
small and medium size business
Requirements
Must have
- product portfolio - just like Zumwarp.com
Nice to have
- ecomerce and mobile app

```html
<!DOCTYPE html>
<html lang="en">
<head>
<meta charset="utf-8">
<title>Kovaridex</title>
<link href="https://fonts.googleapis.com/css2?family=Ubuntu:ital,wght@0,400;0,500;1,400&family=Arimo:ital,wght@0,400;0,700;1,400&display=swap" rel="stylesheet">
<style>
:root{
  --brand:#2c8fe0;
  --hero:#2474bb;
  --hero-dark:#1f69ab;
  --nav:#7d7d7d;
  --nav-line:#9a9a9a;
  --ink:#444;
  --line:#dcdcdc;
  --panel:#efeeee;
  --footer:#1a93ef;
  --footer-bar:#383838;
  --white:#fff;
  --link:#1c8ee6;
  --sky-pale:#eef5fc;
  --sky-mid:#cfe3f5;
}
*{box-sizing:border-box;margin:0;padding:0}
html,body{width:1200px;height:1112px;overflow:hidden;background:var(--white)}
body{position:relative;font-family:"Ubuntu",sans-serif;color:var(--ink)}
.abs{position:absolute}
h2{font-weight:400}

/* header */
.logo{left:239px;top:9px;font-size:32px;letter-spacing:.3px;color:#5a5a5a;line-height:1.1}
.logo span{color:var(--brand)}
.slogan{left:281px;top:51px;font-size:10px;color:#666;letter-spacing:.3px}
.toplinks{left:791px;top:15px;font-size:8px;color:#aaa;letter-spacing:.3px}
.toplinks b{font-weight:400;color:var(--link)}
.search{left:886px;top:8px;width:134px;height:25px;border:1px solid #ccc;font-family:"Arimo",sans-serif;font-size:8px;color:#aaa;padding:8px 10px}
.search svg{position:absolute;right:8px;top:6px}

/* nav */
.nav{left:239px;top:79px;display:flex;height:37px}
.nav a{display:flex;align-items:center;justify-content:center;background:var(--nav);color:var(--white);text-decoration:none;border-right:1px solid var(--nav-line);font-size:12px;letter-spacing:.5px}
.nav a.small{font-size:10px;padding-top:5px}
.nav a.active{background:var(--hero)}

/* hero */
.hero{left:0;top:116px;width:1200px;height:238px;background:var(--hero)}
.hero-side{left:1016px;top:116px;width:184px;height:238px;background:var(--hero-dark);opacity:.35}
.hero-title{left:239px;top:191px;font-size:16px;color:var(--white);line-height:19px;width:240px}
.hero-more{left:240px;top:257px;font-size:16px;color:var(--white);text-decoration:underline;text-underline-offset:3px}
.dots{left:240px;top:319px;display:flex;gap:4px}
.dots i{width:12px;height:12px;border-radius:50%;background:var(--white)}
.dots i.on{background:#3f9ae6}
.hero-art{left:482px;top:136px;width:512px;height:188px;border-radius:6px;
  background:linear-gradient(100deg,rgba(207,227,245,.35) 0%,rgba(207,227,245,.7) 35%,var(--sky-pale) 65%,var(--white) 100%)}

/* intro */
.intro{left:330px;top:381px;width:602px;text-align:center;font-size:12.5px;line-height:20px;color:#555}
.shadow{left:440px;top:470px;width:380px;height:12px;background:radial-gradient(ellipse at 50% 0%,rgba(0,0,0,.28),rgba(0,0,0,0) 70%)}

.section-title{font-size:15.5px;color:#555;letter-spacing:.3px}
.products-title{left:0;width:1290px;top:504px;text-align:center}
.rule{left:239px;top:530px;width:781px;height:1px;background:var(--line)}

/* products */
.card{top:545px;width:176px;height:178px;border:1px solid #d6d6d6;background:var(--white)}
.card .pic{position:absolute;left:14px;top:14px;width:146px;height:112px;border-radius:4px;
  background:linear-gradient(160deg,var(--sky-pale) 0%,var(--sky-mid) 55%,#9cc6ea 100%)}
.card .caption{position:absolute;left:0;bottom:0;width:100%;height:37px;background:var(--panel);font-size:11.5px;color:#555;padding:11px 8px}

/* blogs / testimonials */
.col-title{top:752px}
.post{font-family:"Arimo",sans-serif;font-size:8.2px;line-height:12px;color:#555;border-bottom:1px solid var(--line)}
.blogs{left:240px;top:786px;width:240px}
.blogs .post{padding-bottom:9px;margin-bottom:13px}
.testis{left:533px;top:784px;width:242px}
.testis .post{padding-bottom:6px;margin-bottom:27px}
.by{display:block;color:var(--link);font-style:italic;margin-top:3px}

/* tweet panel */
.tweets{left:794px;top:733px;width:226px;height:214px;background:var(--panel)}
.tweets .head{position:absolute;left:16px;top:25px;display:flex;align-items:center;gap:14px;font-style:italic;font-size:12px;color:#555}
.tweets .head i{width:22px;height:22px;border-radius:50%;background:var(--link)}
.tweets .sep{position:absolute;left:16px;top:57px;width:190px;height:1px;background:#ddd}
.tweet{position:absolute;left:14px;font-family:"Arimo",sans-serif;font-size:7.8px;line-height:10px;color:#666;width:190px}
.tweet a{color:var(--link);text-decoration:none;font-weight:700}
.tweet small{display:block;font-size:5.5px;color:#aaa;margin-top:5px}

/* footer */
.footer{left:0;top:957px;width:1200px;height:119px;background:var(--footer)}
.ft{font-size:12px;color:var(--white);top:985px;letter-spacing:.3px}
.phone{left:240px;top:1005px;width:124px;height:21px;background:var(--white);border-radius:6px;display:flex;align-items:center;gap:8px;padding-left:8px;font-size:12.5px;color:var(--link)}
.address{left:240px;top:1031px;font-family:"Arimo",sans-serif;font-size:6.8px;line-height:8.5px;color:var(--white)}
.flinks{top:1009px;font-family:"Arimo",sans-serif;font-size:7.6px;line-height:12px;color:var(--white)}
.share-label{left:797px;top:989px;font-family:"Arimo",sans-serif;font-size:6.5px;color:var(--white)}
.share{left:798px;top:1011px;display:flex;gap:6px;align-items:center}
.pill{height:11px;border-radius:2px;background:var(--white);font-family:"Arimo",sans-serif;font-size:6px;color:#555;padding:0 4px;display:flex;align-items:center}
.pill.blue{background:#e6eef8}
.pill.red{background:#f05a3c;color:var(--white)}
.join{left:797px;top:1044px;font-family:"Arimo",sans-serif;font-size:6.5px;color:var(--white)}
.circles{left:848px;top:1038px;display:flex;gap:8px}
.circles i{width:20px;height:20px;border-radius:50%;background:#9aa3ad}
.bar{left:0;top:1076px;width:1200px;height:36px;background:var(--footer-bar)}
.copy{left:241px;top:1097px;font-family:"Arimo",sans-serif;font-size:7.6px;color:var(--white)}
.barlinks{left:855px;top:1096px;font-family:"Arimo",sans-serif;font-size:7.8px;color:var(--white);word-spacing:1px}
</style>
</head>
<body>

<header>
  <div class="abs logo">YOUR <span>LOGO</span></div>
  <div class="abs slogan">SLOGAN GOES HERE</div>
  <div class="abs toplinks">LOGIN &nbsp;|&nbsp; <b>GET QUOTE</b></div>
  <div class="abs search">Search
    <svg width="12" height="12" viewBox="0 0 12 12"><circle cx="5" cy="5" r="3.5" fill="none" stroke="#bbb" stroke-width="1.3"/><line x1="7.6" y1="7.6" x2="11" y2="11" stroke="#bbb" stroke-width="1.5"/></svg>
  </div>
  <nav class="abs nav">
    <a class="active" style="width:121px">SOLUTION</a>
    <a style="width:121px">SERVICES</a>
    <a style="width:121px">WHY ?</a>
    <a class="small" style="width:101px">About Us</a>
    <a class="small" style="width:101px">Services</a>
    <a class="small" style="width:102px">Contact Us</a>
  </nav>
</header>

<section>
  <div class="abs hero"></div>
  <div class="abs hero-side"></div>
  <div class="abs hero-title">Lorem Ipsum is simply dummy text of the printing</div>
  <div class="abs hero-more">+read more</div>
  <div class="abs dots"><i class="on"></i><i></i><i></i><i></i></div>
  <div class="abs hero-art" role="img" aria-label="Cloud made of device and document icons"></div>
</section>

<p class="abs intro">Lorem Ipsum is simply dummy text of the printing and typesetting industry. Lorem Ipsum has been the industry's standard dummy text ever since the 1500s, when an unknown printer took a galley of type and scrambled it to make a type specimen book.</p>
<div class="abs shadow"></div>

<h2 class="abs section-title products-title">LATEST PRODUCTS</h2>
<div class="abs rule"></div>

<div class="abs card" style="left:239px"><div class="pic" role="img" aria-label="Cloud with tablet and phone"></div><div class="caption">Lorem Ipsum</div></div>
<div class="abs card" style="left:443px"><div class="pic" role="img" aria-label="Smartphone in front of clouds"></div><div class="caption">Lorem Ipsum</div></div>
<div class="abs card" style="left:644px"><div class="pic" role="img" aria-label="Globe with clouds and app icons"></div><div class="caption">Lorem Ipsum</div></div>
<div class="abs card" style="left:845px"><div class="pic" role="img" aria-label="Cloud with tablet and phone"></div><div class="caption">Lorem Ipsum</div></div>

<h2 class="abs section-title col-title" style="left:240px">OUR BLOGS</h2>
<div class="abs blogs">
  <p class="post">Lorem Ipsum is simply dummy text of the printing and typesetting industry. Lorem Ipsum has been the industry's standard dummy text</p>
  <p class="post">Lorem Ipsum is simply dummy text of the printing and typesetting industry. Lorem Ipsum has been the industry's standard dummy text</p>
  <p class="post">Lorem Ipsum is simply dummy text of the printing and typesetting industry. Lorem Ipsum has been the industry's standard dummy text</p>
</div>

<h2 class="abs section-title col-title" style="left:533px">OUR TESTIMONIALS</h2>
<div class="abs testis">
  <p class="post">Lorem Ipsum is simply dummy text of the printing and typesetting industry. Lorem Ipsum has been the industry's standard dummy text<span class="by">-by admin</span></p>
  <p class="post">Lorem Ipsum is simply dummy text of the printing and typesetting industry. Lorem Ipsum has been the industry's standard dummy text<span class="by">-by admin</span></p>
</div>

<aside class="abs tweets">
  <div class="head"><i></i>LATEST TWEET</div>
  <div class="sep"></div>
  <div class="tweet" style="top:72px"><a>http://chirpline.net/example/abc/link</a><br>Lorem Ipsum is simply dummy text of the printing and typesetting industry<small>2min ago</small></div>
  <div class="tweet" style="top:134px"><a>http://chirpline.net/example/abc/link</a><br>Lorem Ipsum is simply dummy text of the printing and typesetting industry<small>2min ago</small></div>
</aside>

<footer>
  <div class="abs footer"></div>
  <div class="abs ft" style="left:240px">CONTACT US</div>
  <div class="abs phone">
    <svg width="14" height="14" viewBox="0 0 14 14"><circle cx="7" cy="7" r="6.2" fill="none" stroke="#1c8ee6" stroke-width="1"/><path d="M4.6 3.8c.4-.3.8-.3 1 .1l.6 1.1c.2.3.1.6-.2.8l-.4.3c.4.9 1.1 1.6 2 2l.3-.4c.2-.3.5-.4.8-.2l1.1.6c.4.2.4.6.1 1-.6.8-1.4.9-2.3.5-1.6-.7-2.8-1.900-3.5-3.5-.4-.9-.3-1.7.5-2.3z" fill="#1c8ee6"/></svg>
    123 - 456 - 7890
  </div>
  <div class="abs address">#123 Example, Street<br>UK 1234<br>UK</div>

  <div class="abs ft" style="left:479px">SOLUTION</div>
  <div class="abs flinks" style="left:481px">Lorem Ipsum<br>Lorem Ipsum<br>Lorem Ipsum<br>Lorem Ipsum<br>Lorem Ipsum</div>

  <div class="abs ft" style="left:639px">SERVICES</div>
  <div class="abs flinks" style="left:639px">Lorem Ipsum<br>Lorem Ipsum<br>Lorem Ipsum<br>Lorem Ipsum<br>Lorem Ipsum</div>

  <div class="abs share-label">SHARE</div>
  <div class="abs share">
    <span class="pill blue">Like</span><span class="pill">3k</span>
    <span class="pill blue">Post</span><span class="pill">316</span>
    <span class="pill blue">+1</span><span class="pill">3k</span>
    <span class="pill red">Share</span><span class="pill">4.6K</span>
  </div>
  <div class="abs join">JOIN US</div>
  <div class="abs circles"><i></i><i></i><i></i></div>

  <div class="abs bar"></div>
  <div class="abs copy">Copyright All Right Reserved.</div>
  <div class="abs barlinks">Lorem Ipsum &nbsp;|&nbsp; Lorem Ipsum &nbsp;|&nbsp; Lorem Ipsum</div>
</footer>

</body>
</html>
```